General Contractors need a new Crisp updated Card Design

We need a new business card design for our company of 25 years based in Toronto call Holvaster Building Inc. : Our goal is to be the leading commercial contractors in Toronto by providing exceptional value to our clients. We work very hard to deliver professional, quality, service in conjunction with consistent price competitiveness to all of our clients on every single project.

Target Market(s)

Design & Build Clients

Industry/Entity Type

Construction Company

Contact Information for Business Card

Address:
18 North Tamlin Glen Road, Unit 57, Marbrook Vale, ON, K7T 2R9
Office: 905-218-5937

Holvasters Logo
Employee Job Description
Employee Cell Phone #
Employee Email
www.holvaster-example.com

Colors

Designer to choose colors to be used in the design.

Requirements
Must have
• Quote Company Saying:
• "Professional. Quality. Service."
Nice to have
• New Crisp up to date look. simple & fresh ( Not to Busy)
Should not have
• NO BLUE PRINTS ON THE BUSINESS CARDS

```html
<!DOCTYPE html>
<html lang="en">
<head>
<meta charset="utf-8">
<title>Holvaster Building Inc. – Business Card</title>
<link rel="stylesheet" href="https://fonts.googleapis.com/css2?family=Roboto+Condensed:wght@700&family=Tinos:wght@400&display=swap">
<style>
  :root {
    --brand-green: #1f9a55;
    --tint-mid: #8dcaa6;
    --tint-light: #d3ebdd;
    --paper: #ffffff;
    --ink: #1f2a22;
  }
  * { margin: 0; padding: 0; box-sizing: border-box; }
  html, body {
    width: 1200px; height: 1200px; overflow: hidden;
    background: var(--paper);
  }
  .canvas { position: relative; width: 1200px; height: 1200px; }

  .card {
    position: absolute;
    left: 285px; width: 630px; height: 362px;
    border: 2.5px solid var(--brand-green);
    background: var(--paper);
  }
  .card--front { top: 210px; }
  .card--back  { top: 593px; }

  /* front */
  .brand {
    position: absolute; left: 58px; top: 38px;
    display: flex; align-items: center; gap: 22px;
  }
  .brand__square {
    width: 110px; height: 110px;
    background: var(--brand-green);
  }
  .brand__name {
    font-family: "Roboto Condensed", sans-serif;
    font-weight: 700;
    color: var(--brand-green);
    font-size: 52px; line-height: 1.05;
    letter-spacing: 1px;
    text-transform: uppercase;
  }
  .tagline {
    position: absolute; left: 66px; top: 296px;
    font-family: "Roboto Condensed", sans-serif;
    font-weight: 700;
    color: var(--brand-green);
    font-size: 27px;
    letter-spacing: 5.2px;
    text-transform: uppercase;
    white-space: nowrap;
  }

  /* back */
  .back__panel {
    position: absolute; left: 36px; top: 36px;
    width: 273px; height: 275px;
    background: linear-gradient(180deg, var(--tint-mid) 0%, var(--tint-light) 100%);
  }
  .contact {
    position: absolute; left: 326px; top: 46px;
    font-family: "Tinos", serif;
    color: var(--ink);
    font-size: 17.5px; line-height: 22.5px;
  }
  .contact p { white-space: nowrap; }
  .contact .gap { margin-top: 30px; }
  .contact .label { display: inline-block; width: 58px; }
  .contact .web { letter-spacing: 2px; }
</style>
</head>
<body>
<main class="canvas">
  <section class="card card--front" aria-label="Card front">
    <div class="brand">
      <div class="brand__square"></div>
      <div class="brand__name">Holvaster<br>Building Inc.</div>
    </div>
    <p class="tagline">Professional. Quality. Service.</p>
  </section>

  <section class="card card--back" aria-label="Card back">
    <div class="back__panel" role="img" aria-label="Large light green brand panel"></div>
    <div class="contact">
      <p>John Doe - Manager, CEO</p>
      <p class="gap"><span class="label">Phone:</span>416-730-2849</p>
      <p><span class="label">Fax:</span>905-218-5940</p>
      <p><span class="label">Email:</span>sh@holvaster-example.com</p>
      <p class="gap">Head Office:</p>
      <p>18 North Tamlin Glen Road, Unit 57</p>
      <p>Marbrook Vale, ON, K7T 2R9</p>
      <p class="gap web">www.holvaster-example.com</p>
    </div>
  </section>
</main>
</body>
</html>
```